R&T Builders and Spaces Business Card

We need to redesign our business card. We had used white vellum wih grey logo and txt in the past. I would like to bring a little life into our cards without being over the top. I think I will be going away from the vellum and printing soft touch business cards.
I have attached what we currently have and our new logo design.

```html
<!DOCTYPE html>
<html lang="en">
<head>
<meta charset="utf-8">
<title>R&amp;T Builders and Spaces — Business Card</title>
<link href="https://fonts.googleapis.com/css2?family=Lato:wght@300;400;700;900&display=swap" rel="stylesheet">
<style>
  :root {
    --backdrop: #8e8e8e;
    --card: #3a3a3c;
    --ink-light: #ffffff;
    --ink-dark: #3a3a3c;
  }
  html, body {
    margin: 0;
    padding: 0;
    width: 1200px;
    height: 1200px;
    overflow: hidden;
    background: var(--backdrop);
    font-family: "Lato", Arial, sans-serif;
  }
  .card {
    position: absolute;
    left: 281px;
    width: 641px;
    height: 365px;
    border-radius: 32px;
    background: var(--card);
    overflow: hidden;
    color: var(--ink-light);
  }
  .card--front { top: 195px; }
  .card--back { top: 639px; }

  .identity {
    position: absolute;
    right: 348px;
    top: 130px;
    text-align: right;
  }
  .identity__name {
    margin: 0;
    font-weight: 900;
    font-size: 34px;
    line-height: 1;
    letter-spacing: -0.5px;
  }
  .identity__title {
    margin: 6px 7px 0 0;
    font-size: 17px;
    font-weight: 400;
  }
  .divider {
    position: absolute;
    left: 316px;
    top: 109px;
    width: 1px;
    height: 110px;
    background: var(--ink-light);
    opacity: 0.8;
  }
  .contact {
    position: absolute;
    left: 345px;
    top: 104px;
    margin: 0;
    padding: 0;
    list-style: none;
    font-size: 15px;
    line-height: 22px;
  }
  .contact__item {
    position: relative;
    padding-left: 22px;
    margin-bottom: 6px;
  }
  .contact__item--tight { margin-bottom: 1px; }
  .contact__icon {
    position: absolute;
    left: 0;
    top: 5px;
    width: 12px;
    height: 12px;
    fill: var(--ink-light);
  }
  .web-band {
    position: absolute;
    left: 0;
    top: 288px;
    width: 543px;
    height: 43px;
    background: var(--ink-light);
    color: var(--ink-dark);
    font-size: 15px;
    letter-spacing: 3px;
    line-height: 43px;
    text-align: center;
    padding-left: 60px;
    box-sizing: border-box;
  }
  .band-square {
    position: absolute;
    top: 288px;
    left: 551px;
    width: 42px;
    height: 43px;
    background: var(--ink-light);
  }
  .band-end {
    position: absolute;
    top: 288px;
    left: 600px;
    width: 41px;
    height: 43px;
    background: var(--ink-light);
  }

  .brand {
    position: absolute;
    left: 0;
    right: 0;
    top: 71px;
    text-align: center;
  }
  .brand__square {
    display: block;
    width: 220px;
    height: 220px;
    margin: 0 auto;
    background: var(--ink-light);
  }
  .brand__name {
    margin: 14px 0 0;
    font-weight: 300;
    font-size: 19px;
    letter-spacing: 3px;
  }
</style>
</head>
<body>
  <section class="card card--front">
    <div class="identity">
      <h1 class="identity__name">DALE M. HARLOW</h1>
      <p class="identity__title">Principal</p>
    </div>
    <div class="divider"></div>
    <ul class="contact">
      <li class="contact__item contact__item--tight">
        <svg class="contact__icon" viewBox="0 0 12 12"><path d="M6 0a4 4 0 0 0-4 4c0 3 4 8 4 8s4-5 4-8a4 4 0 0 0-4-4zm0 5.6A1.6 1.6 0 1 1 6 2.4a1.6 1.6 0 0 1 0 3.2z"/></svg>
        1480 W Mesa Ridge Rd, Suite 200
      </li>
      <li class="contact__item">Tempe, Arizona 85281</li>
      <li class="contact__item contact__item--tight">
        <svg class="contact__icon" viewBox="0 0 12 12"><path d="M2.4 0.5l2 2.2-1 1.6c.8 1.6 2 2.8 3.6 3.6l1.6-1 2.2 2-1.2 2.4C4.8 11 1 7.2.2 2z"/></svg>
        480 555 0142
      </li>
      <li class="contact__item contact__item--tight">
        <svg class="contact__icon" viewBox="0 0 12 12"><path d="M3 0h6a1 1 0 0 1 1 1v10a1 1 0 0 1-1 1H3a1 1 0 0 1-1-1V1a1 1 0 0 1 1-1zm.6 1.4v8h4.8v-8zM6 10a.6.6 0 1 0 0 1.2A.6.6 0 0 0 6 10z"/></svg>
        480 555 0187
      </li>
      <li class="contact__item">
        <svg class="contact__icon" viewBox="0 0 12 12"><path d="M0 2.5h12v7H0zm1 1v.3l5 3 5-3v-.3z"/></svg>
        dale@rtbuilders.com
      </li>
    </ul>
    <div class="web-band">WWW.RTBUILDERS.COM</div>
    <div class="band-square"></div>
    <div class="band-end"></div>
  </section>

  <section class="card card--back">
    <div class="brand">
      <span class="brand__square"></span>
      <p class="brand__name">R&amp;T BUILDERS AND SPACES</p>
    </div>
  </section>
</body>
</html>
```